Corvane Stationery Design

We need design for our stationary, including:
1) Letterhead
- A4/Letter size in landscape and portrait letterhead
- The letterhead must be in a word file, and the address should be editable using the Felixti or Perpetua Titling TTF
- The output file should be in .docx and in .ai.
2) Business card
- The business card will be printed in white paper and single face only, so there should be nothing on the reverse side.
3) Envelope (sizes A4, Letter, and small document)
Please refer to the picture showing some samples of stationary with designs that would fulfill our wish.
We're including the logo in .AI.
Thanks
Target Market(s)
High end investors
Industry/Entity Type
Landscape
Look and feel

```html
<!DOCTYPE html>
<html lang="en">
<head>
<meta charset="utf-8">
<title>Corvane Business Card</title>
<link rel="stylesheet" href="https://fonts.googleapis.com/css2?family=Cinzel:wght@400;700&family=Cormorant+Garamond:wght@500&display=swap">
<style>
  :root {
    --backdrop: #e6e7e9;
    --card: #f7f7f8;
    --brand-blue: #1f6f9c;
    --ink: #2b2b2d;
    --muted: #6b6c70;
    --icon: #8a8b8f;
  }
  * { box-sizing: border-box; margin: 0; padding: 0; }
  html, body { width: 1200px; height: 955px; overflow: hidden; }
  body {
    background: var(--backdrop);
    display: flex;
    align-items: center;
    justify-content: center;
  }
  .business-card {
    position: relative;
    width: 840px;
    height: 480px;
    background: var(--card);
    box-shadow: 0 10px 30px rgba(0,0,0,0.12);
  }
  .brand-name {
    position: absolute;
    left: 72px;
    top: 170px;
    font-family: "Cinzel", serif;
    font-weight: 400;
    font-size: 64px;
    letter-spacing: 4px;
    color: var(--brand-blue);
    text-transform: uppercase;
  }
  .contact-block {
    position: absolute;
    right: 64px;
    top: 150px;
    text-align: right;
    font-family: "Cormorant Garamond", serif;
    color: var(--muted);
  }
  .corner-marker {
    position: absolute;
    right: -22px;
    top: -4px;
    width: 14px;
    height: 14px;
  }
  .person-name {
    font-family: "Cinzel", serif;
    font-weight: 700;
    font-size: 19px;
    color: var(--ink);
    letter-spacing: 1px;
  }
  .person-title {
    font-family: "Cinzel", serif;
    font-size: 11px;
    letter-spacing: 1px;
    margin: 6px 0 10px;
  }
  .contact-line {
    display: flex;
    align-items: center;
    justify-content: flex-end;
    gap: 8px;
    font-family: "Cinzel", serif;
    font-size: 11px;
    letter-spacing: 0.5px;
    line-height: 20px;
  }
  .contact-icon { width: 10px; height: 10px; flex: none; }
</style>
</head>
<body>
  <article class="business-card">
    <div class="brand-name">Corvane</div>

    <div class="contact-block">
      <svg class="corner-marker" viewBox="0 0 14 14" aria-hidden="true">
        <polygon points="14,0 14,14 0,7" fill="var(--brand-blue)"/>
      </svg>
      <div class="person-name">ELIAS MARLOW</div>
      <div class="person-title">GENERAL MANAGER</div>
      <div class="contact-line">
        <span>0412 555 019</span>
        <svg class="contact-icon" viewBox="0 0 10 10" aria-hidden="true">
          <rect x="2" y="0.5" width="6" height="9" rx="1" fill="none" stroke="var(--icon)" stroke-width="1"/>
        </svg>
      </div>
      <div class="contact-line">
        <span>ELIAS@CORVANE.COM</span>
        <svg class="contact-icon" viewBox="0 0 10 10" aria-hidden="true">
          <rect x="0.5" y="1.5" width="9" height="7" fill="var(--icon)"/>
        </svg>
      </div>
      <div class="contact-line">
        <span>WWW.CORVANE.COM</span>
        <svg class="contact-icon" viewBox="0 0 10 10" aria-hidden="true">
          <circle cx="5" cy="5" r="4.5" fill="var(--icon)"/>
        </svg>
      </div>
    </div>
  </article>
</body>
</html>
```